Stationery Design Project

KT7 Staffing requires letterhead and business card designs for a company based in London. Just like the name, we're a management resourcing company, providing resources to third party companies. You can see www.kt7staffing-example.com for ideas on existing colour schemes and design concepts that have been implimented and agreed to. Ultimately the design should broadcast professionalism, safety and the concept of growth.

Target Market(s)

Financial institutes; friendly societies (All UK based)

Industry/Entity Type

Safety

Requirements
Must have
• Files produced should be print ready; and the text in them editable (eg address, name etc)

```html
<!DOCTYPE html>
<html lang="en">
<head>
<meta charset="utf-8">
<title>KT7 Staffing – Stationery</title>
<link href="https://fonts.googleapis.com/css2?family=Arimo:wght@400;500;700&display=swap" rel="stylesheet">
<style>
  :root {
    --teal: #1b9fb0;
    --teal-dark: #1a8e99;
    --sky: #7bbfdc;
    --sky-text: #5fb4d8;
    --grey: #8a8a8a;
    --paper: #ffffff;
    --edge: #c9c9c9;
  }
  * { margin: 0; padding: 0; box-sizing: border-box; }
  html, body { width: 1200px; height: 900px; overflow: hidden; background: var(--paper); }
  body { position: relative; font-family: "Arimo", Arial, sans-serif; }

  .sheet {
    position: absolute; background: var(--paper);
    border: 1px solid var(--edge);
    box-shadow: 1px 1px 2px rgba(0,0,0,0.35);
    overflow: hidden;
  }
  .letterhead { left: 94px; top: 24px; width: 596px; height: 842px; }
  .card { width: 250px; height: 157px; top: 424px; }
  .card--front { left: 585px; }
  .card--back { left: 840px; }

  .brand { position: absolute; display: flex; align-items: center; color: var(--teal-dark); font-weight: 500; white-space: nowrap; }
  .brand__mark { background: var(--sky); margin-right: 0.35em; }

  .letterhead .brand { left: 20px; top: 36px; font-size: 36px; }
  .letterhead .brand__mark { width: 26px; height: 26px; }

  .rule { position: absolute; width: 1px; background: var(--sky); }
  .letterhead .rule--a { left: 288px; top: 26px; height: 50px; }
  .letterhead .rule--b { left: 449px; top: 26px; height: 50px; }

  .contact { position: absolute; font-size: 8px; line-height: 12px; }
  .contact dt { position: absolute; color: var(--teal-dark); font-weight: 500; }
  .contact dd { color: var(--sky-text); white-space: nowrap; }

  .letterhead .contact--address { left: 300px; top: 30px; }
  .letterhead .contact--address dt { left: 0; }
  .letterhead .contact--address dd { margin-left: 37px; }
  .letterhead .contact--lines { left: 448px; top: 30px; }
  .letterhead .contact--lines .row { display: flex; }
  .letterhead .contact--lines dt { position: static; width: 39px; text-align: right; }
  .letterhead .contact--lines dd { margin-left: 6px; }

  .wave { position: absolute; left: 0; bottom: 0; width: 100%; display: block; }
  .wave .wave__light { fill: var(--sky); }
  .wave .wave__band { fill: var(--teal); }

  .web { position: absolute; color: #fff; font-weight: 700; white-space: nowrap; }
  .letterhead .web { left: 0; right: 0; bottom: 14px; text-align: center; font-size: 10px; }

  .card--front .brand { left: 0; right: 0; top: 50px; justify-content: center; font-size: 25px; }
  .card--front .brand__mark { width: 18px; height: 18px; }

  .card--back .brand { left: 17px; top: 14px; font-size: 16px; }
  .card--back .brand__mark { width: 12px; height: 12px; }
  .holder { position: absolute; right: 14px; top: 65px; font-size: 11px; font-weight: 700; color: var(--sky-text); letter-spacing: 0.2px; }

  .card--back .contact { font-size: 6.5px; line-height: 10.5px; top: 91px; }
  .card--back .contact dd { color: var(--grey); }
  .card--back .contact--address { left: 17px; }
  .card--back .contact--address dt { left: 0; }
  .card--back .contact--address dd { margin-left: 29px; }
  .card--back .contact--lines { left: 130px; }
  .card--back .contact--lines .row { display: flex; }
  .card--back .contact--lines dt { position: static; width: 31px; text-align: right; }
  .card--back .contact--lines dd { margin-left: 4px; }
  .card--back .web { left: 17px; bottom: 7px; font-size: 7px; }
</style>
</head>
<body>

<section class="sheet letterhead" aria-label="Letterhead">
  <div class="brand"><span class="brand__mark"></span>KT7 Staffing</div>
  <span class="rule rule--a"></span>
  <dl class="contact contact--address">
    <dt>Address</dt>
    <dd>Harwell Park Rd</dd>
    <dd>Ambleside Vale</dd>
    <dd>Cumbria LA99 4QZ England</dd>
  </dl>
  <span class="rule rule--b"></span>
  <dl class="contact contact--lines">
    <div class="row"><dt>Phone</dt><dd>+44 20 7946 0123</dd></div>
    <div class="row"><dt>Fax</dt><dd>+44 20 7946 0456</dd></div>
    <div class="row"><dt>Email</dt><dd>info@kt7-example.com</dd></div>
  </dl>
  <svg class="wave" viewBox="0 0 596 50" height="50" preserveAspectRatio="none" aria-hidden="true">
    <path class="wave__light" d="M0 14 Q298 -8 596 14 V50 H0 Z"/>
    <path class="wave__band" d="M0 27 Q298 2 596 27 V50 H0 Z"/>
  </svg>
  <p class="web">www.kt7staffing-example.com</p>
</section>

<section class="sheet card card--front" aria-label="Business card front">
  <div class="brand"><span class="brand__mark"></span>KT7 Staffing</div>
  <svg class="wave" viewBox="0 0 250 30" height="30" preserveAspectRatio="none" aria-hidden="true">
    <path class="wave__light" d="M0 8 Q125 -4 250 4 V30 H0 Z"/>
    <path class="wave__band" d="M0 12 Q125 1 250 9 V30 H0 Z"/>
  </svg>
</section>

<section class="sheet card card--back" aria-label="Business card back">
  <div class="brand"><span class="brand__mark"></span>KT7 Staffing</div>
  <p class="holder">DANIEL HART</p>
  <dl class="contact contact--address">
    <dt>address</dt>
    <dd>Harwell Park Rd</dd>
    <dd>Ambleside Vale</dd>
    <dd>Cumbria LA99 4QZ England</dd>
  </dl>
  <dl class="contact contact--lines">
    <div class="row"><dt>phone</dt><dd>+44 20 7946 0123</dd></div>
    <div class="row"><dt>fax</dt><dd>+44 20 7946 0456</dd></div>
    <div class="row"><dt>email</dt><dd>info@kt7-example.com</dd></div>
  </dl>
  <svg class="wave" viewBox="0 0 250 30" height="30" preserveAspectRatio="none" aria-hidden="true">
    <path class="wave__light" d="M0 4 Q125 -4 250 8 V30 H0 Z"/>
    <path class="wave__band" d="M0 9 Q125 1 250 12 V30 H0 Z"/>
  </svg>
  <p class="web">www.kt7staffing-example.com</p>
</section>

</body>
</html>
```